Our Crooked Plot: Need a label for bee and garden related products

We want to distribute some homemade goods from our bees and greenhouse garden to friends, family, and neighbors. Things like honey, beeswax candles, lip balm, tomato sauce, pickles, etc. The yard itself is also a bit odd as it's almost an acre, but it's really long and narrow. We'd like to call it "Our Crooked Plot". We're open to a variety of designs and really don't have specific preferences just yet.

Font styles to use
Serif
Decorative
Script

Requirements
Must have
• The company name, Our Crooked Plot.

```html
<!DOCTYPE html>
<html lang="en">
<head>
<meta charset="utf-8">
<title>Our Crooked Plot – Product Labels</title>
<link href="https://fonts.googleapis.com/css2?family=Cinzel:wght@700;900&display=swap" rel="stylesheet">
<style>
  :root {
    --backdrop: #ebe6e0;
    --gold: #c9a548;
    --gold-deep: #9c7a30;
    --forest: #0b2b14;
    --claret: #5c0000;
    --walnut: #2b1405;
  }
  * { margin: 0; padding: 0; box-sizing: border-box; }
  html, body { width: 1200px; height: 900px; overflow: hidden; }
  body { background: var(--backdrop); position: relative; font-family: "Cinzel", Georgia, serif; }

  .label { position: absolute; top: 218px; width: 320px; height: 464px; }
  .label--candle { left: 80px; --fill: var(--forest); }
  .label--sauce { left: 441px; --fill: var(--claret); }
  .label--honey { left: 801px; --fill: var(--walnut); }

  .label__shape { position: absolute; inset: 0; width: 320px; height: 464px; }
  .label__body { fill: var(--fill); }
  .label__rule { fill: none; stroke: var(--gold); stroke-width: 1.6; }

  .label__art {
    position: absolute; left: 66px; top: 56px; width: 190px; height: 212px;
    border-radius: 50% 50% 22% 22% / 46% 46% 12% 12%;
    background: radial-gradient(ellipse 60% 55% at 50% 40%, var(--gold) 0%, var(--gold-deep) 70%, rgba(156,122,48,0.55) 100%);
  }

  .label__brand {
    position: absolute; left: 0; right: 0; top: 284px;
    text-align: center; color: var(--gold);
    font-size: 31px; font-weight: 900; line-height: 35px; letter-spacing: 0.5px;
  }

  .label__product {
    position: absolute; left: 0; right: 0;
    text-align: center; color: var(--gold);
    font-size: 20px; font-weight: 700; line-height: 24px; letter-spacing: 1px;
  }
  .label__product--two-line { top: 371px; }
  .label__product--one-line { top: 383px; }
</style>
</head>
<body>

<div class="label label--candle">
  <svg class="label__shape" viewBox="0 0 320 464" aria-hidden="true">
    <path class="label__body" d="M0 52 H55 C68 14 112 0 160 0 C208 0 252 14 265 52 H320 V412 H265 C252 450 208 464 160 464 C112 464 68 450 55 412 H0 Z"/>
    <path class="label__rule" d="M12 64 H66 C78 26 118 12 160 12 C202 12 242 26 254 64 H308 V400 H254 C242 438 202 452 160 452 C118 452 78 438 66 400 H12 Z"/>
  </svg>
  <div class="label__art" role="img" aria-label="Gold line drawing of a tree with a hanging beehive over a grassy mound"></div>
  <div class="label__brand">Our Crooked<br>Plot</div>
  <div class="label__product label__product--two-line">BEESWAX<br>CANDLE</div>
</div>

<div class="label label--sauce">
  <svg class="label__shape" viewBox="0 0 320 464" aria-hidden="true">
    <path class="label__body" d="M0 52 H55 C68 14 112 0 160 0 C208 0 252 14 265 52 H320 V412 H265 C252 450 208 464 160 464 C112 464 68 450 55 412 H0 Z"/>
    <path class="label__rule" d="M12 64 H66 C78 26 118 12 160 12 C202 12 242 26 254 64 H308 V400 H254 C242 438 202 452 160 452 C118 452 78 438 66 400 H12 Z"/>
  </svg>
  <div class="label__art" role="img" aria-label="Gold line drawing of a tree with a hanging beehive over a grassy mound"></div>
  <div class="label__brand">Our Crooked<br>Plot</div>
  <div class="label__product label__product--two-line">TOMATO<br>SAUCE</div>
</div>

<div class="label label--honey">
  <svg class="label__shape" viewBox="0 0 320 464" aria-hidden="true">
    <path class="label__body" d="M0 52 H55 C68 14 112 0 160 0 C208 0 252 14 265 52 H320 V412 H265 C252 450 208 464 160 464 C112 464 68 450 55 412 H0 Z"/>
    <path class="label__rule" d="M12 64 H66 C78 26 118 12 160 12 C202 12 242 26 254 64 H308 V400 H254 C242 438 202 452 160 452 C118 452 78 438 66 400 H12 Z"/>
  </svg>
  <div class="label__art" role="img" aria-label="Gold line drawing of a tree with a hanging beehive over a grassy mound"></div>
  <div class="label__brand">Our Crooked<br>Plot</div>
  <div class="label__product label__product--one-line">HONEY</div>
</div>

</body>
</html>
```